Dynamic Business Card for Sports Supplements Company

Hi! I'm looking for an awesome business card to match my existing sports supplement company. I have uploaded my current company logo and screenshot of the front page of my website.

I would like to have something dynamic and interesting and utilize the colors in the website - the reds and purples

The business card should be double sided and focus on a unique eye-catching design on the back and include all the relevant company info.

Most importantly, it should say somewhere: "Sign up on our website for a coupon code."

Target Market(s)

Mostly for women gym goers but it shouldn't be too feminine. It should be in keeping with the website design. It should flow and clearly be connected to it

Industry/Entity Type

Business

Contact Information for Business Card

Lorena K. Vasquez
CEO
LVasquez@Fortivanco.example
www.fortivanco.example
614.275.3081
P.O. Box 48317
Larkmoor, Vermont 22417

Sign up on our website for a coupon code

Font styles to use
Serif
Sans Serif
Other font styles liked:
• Novecento font family and "Fortivan" is in AR Destine font

Requirements
Must have
• One side should be a bold Fortivan logo design. Even just the symbol itself may be o.k. (see attached file)

```html
<!DOCTYPE html>
<html lang="en">
<head>
<meta charset="utf-8">
<title>Fortivan Business Card</title>
<link rel="stylesheet" href="https://fonts.googleapis.com/css2?family=Figtree:wght@400;500;700;800&display=swap">
<style>
  :root {
    --backdrop: #2e2e30;
    --purple-light: #654a91;
    --purple-dark: #3a2d61;
    --white: #ffffff;
    --ink: #141414;
    --grey: #6b6b6b;
    --red: #e0202a;
  }
  html, body {
    margin: 0;
    width: 1200px;
    height: 855px;
    overflow: hidden;
    background: var(--backdrop);
    font-family: "Figtree", sans-serif;
  }
  .canvas { position: relative; width: 1200px; height: 855px; }
  .card {
    position: absolute;
    left: 354px;
    width: 492px;
  }
  .card-front {
    top: 137px;
    height: 281px;
    background: radial-gradient(ellipse 60% 70% at 50% 45%, var(--purple-light), var(--purple-dark));
  }
  .brand-ring {
    position: absolute;
    left: 188px; top: 82px;
    width: 100px; height: 100px;
    border: 8px solid var(--white);
    border-radius: 50%;
    display: flex; align-items: center; justify-content: center;
  }
  .brand-ring-name {
    color: var(--white);
    font-weight: 800;
    font-size: 17px;
    letter-spacing: 0.5px;
    text-transform: uppercase;
  }
  .coupon-note {
    position: absolute;
    left: 0; right: 0; top: 240px;
    text-align: center;
    color: var(--white);
    font-size: 13px;
    font-weight: 400;
    margin: 0;
  }
  .card-back { top: 430px; height: 288px; background: var(--white); }
  .brand-lockup {
    position: absolute;
    left: 302px; top: 28px;
    width: 164px;
    display: flex; flex-direction: column; align-items: center; gap: 14px;
  }
  .brand-square { width: 62px; height: 62px; background: var(--red); }
  .brand-name {
    color: var(--ink);
    font-weight: 800;
    font-size: 24px;
    letter-spacing: 1px;
    text-transform: uppercase;
    line-height: 1;
  }
  .person { position: absolute; left: 25px; top: 119px; }
  .person-name { margin: 0; font-size: 18px; font-weight: 500; color: var(--ink); line-height: 1.1; }
  .person-title { margin: 1px 0 0; font-size: 13px; color: var(--grey); line-height: 17px; }
  .address { position: absolute; left: 25px; top: 168px; margin: 0; font-style: normal; font-size: 13px; line-height: 17px; color: var(--grey); }
  .contacts { position: absolute; left: 25px; top: 214px; margin: 0; padding: 0; list-style: none; font-size: 13px; line-height: 17px; color: var(--grey); }
  .contacts li { display: flex; align-items: center; gap: 5px; }
  .contacts svg { width: 11px; height: 11px; flex: none; }
</style>
</head>
<body>
<div class="canvas">
  <section class="card card-front">
    <div class="brand-ring"><span class="brand-ring-name">Fortivan</span></div>
    <p class="coupon-note">Sign up on our website for a coupon code</p>
  </section>

  <section class="card card-back">
    <div class="brand-lockup">
      <div class="brand-square"></div>
      <div class="brand-name">Fortivan</div>
    </div>
    <div class="person">
      <h1 class="person-name">Lorena K. Vasquez</h1>
      <p class="person-title">CEO</p>
    </div>
    <address class="address">P.O. Box 48317<br>Larkmoor, Vermont 22417</address>
    <ul class="contacts">
      <li>
        <svg viewBox="0 0 12 12" aria-hidden="true"><path d="M2.5 11 C1 9 1 5 4 2.5 L6 1 L7.5 3 L5.5 4.5 C4.3 5.8 4 7.5 4.5 9 L6.5 8.5 L7.3 10.8 L4.5 11.8 Z" fill="var(--red)"/></svg>
        614.275.3081
      </li>
      <li>
        <svg viewBox="0 0 12 12" aria-hidden="true"><rect x="0.5" y="2.5" width="11" height="7" fill="var(--red)"/><path d="M0.5 2.5 L6 6.5 L11.5 2.5 M0.5 9.5 L4.5 5.5 M11.5 9.5 L7.5 5.5" stroke="var(--white)" stroke-width="0.9" fill="none"/></svg>
        LVasquez@Fortivanco.example
      </li>
      <li>
        <svg viewBox="0 0 12 12" aria-hidden="true"><g fill="none" stroke="var(--red)" stroke-width="1.1"><circle cx="6" cy="6" r="5"/><ellipse cx="6" cy="6" rx="2.2" ry="5"/><path d="M1 6 H11 M1.8 3.5 H10.2 M1.8 8.5 H10.2"/></g></svg>
        www.fortivanco.example
      </li>
    </ul>
  </section>
</div>
</body>
</html>
```